Tallow Ridge Bars needs a bar wrapper design

Tallow Ridge Bars is looking for a wrapper design for our flagship protein bar. A sleek and simple, yet powerful design is a must. A company that has a no BS attitude, no flashy artwork and straight to the point advertising is key. Focusing on Bodybuilders and Powerlifters, the wrapper does not need to appeal to the mass market. A dark, simple, and powerful vibe must be achieved. Less is more

Target Market(s)

Body Builders and Powerlifters

Industry/Entity Type

Supplement

Font styles to use
Decorative

Colors

Designer to choose colors to be used in the design.

Requirements
Must have
• Refer to "Legal Label Requirements" document.
• Refer to "Template Drawn" or "Wrapper.ai" for dimensions.
• *Must have the "Tallow Bar" logo stamped somewhere on the front of the bar**
• Sleek and powerful design
• Neutral /dark colors and possible accents with logo colors (use sparingly)
• Flavor of bar "Maple Oat Crunch" must be displayed somewhere. Simple graphic can be included if goes well with overall design.
• Wrapper will be foil, so please make use of metallic effects by leaving sections/outlines transparent.
• Claims: (State it uses "Hydrolyzed Whey Protein" and contains 25g's of protein and only 6g's of sugar, as well as only real ingredients (These must be in French as well)
• Proudly Canadian stamp with flag somewhere.
• Social Media Icons (Instagram,Facebook) as well as website "tallowbarco.ca)
• Design must be able to work with future bar flavors, with only altering colors/flavor graphic (if necessary)
• *Will Include Nutritional Label and Ingredient List at a later date*
Nice to have
• I think a cool graphic of a simple hand and hammer outline using the metallic effect would be cool. Something that resembles the act of "forging metal" while demonstrating power, but isn't too distracting.
• A label mock up to see a general bar idea
Should not have
• Flashy/godly designs

```html
<!DOCTYPE html>
<html lang="en">
<head>
<meta charset="utf-8">
<title>Tallow Bar – Wrapper</title>
<link rel="stylesheet" href="https://fonts.googleapis.com/css2?family=Open+Sans:wght@400;600;700;800&family=Oswald:wght@500&display=swap">
<style>
  :root {
    --page: #ffffff;
    --wrap-black: #0a0a0a;
    --wrap-edge: #1c1c1c;
    --accent-red: #e0262a;
    --logo-grey: #d4d4d4;
    --text-white: #ffffff;
    --ember: #ff7a1a;
    --ember-deep: #7a1e08;
  }
  * { box-sizing: border-box; margin: 0; padding: 0; }
  html, body { width: 1000px; height: 1200px; overflow: hidden; background: var(--page); }
  body { position: relative; font-family: "Open Sans", Arial, sans-serif; color: var(--text-white); }

  .wrapper-front { position: absolute; left: 0; top: 0; width: 1000px; height: 520px; }
  .wrapper-front svg { position: absolute; left: 0; top: 0; }

  .flat-label { position: absolute; left: 93px; top: 575px; width: 812px; height: 585px; background: var(--wrap-black); overflow: hidden; }
  .flat-label .seam { position: absolute; left: 0; right: 0; height: 1px; background: #1d1d1d; }
  .flat-label .seam-side { position: absolute; top: 0; bottom: 0; width: 1px; background: #1d1d1d; }

  .forge-scene { position: absolute; border-radius: 4px; }
  .label-scene {
    left: 340px; top: 60px; width: 472px; height: 380px;
    background:
      radial-gradient(ellipse 120px 38px at 280px 300px, rgba(255,190,80,.95), rgba(255,110,20,.7) 45%, rgba(120,30,5,0) 100%),
      radial-gradient(ellipse 260px 170px at 300px 230px, rgba(90,40,20,.55), rgba(10,10,10,0) 80%),
      linear-gradient(90deg, var(--wrap-black), rgba(10,10,10,0) 35%);
  }

  .brand-frame { position: absolute; border: 3px solid var(--accent-red); border-radius: 10px; display: flex; align-items: center; justify-content: center; }
  .brand-name { font-family: "Open Sans", Arial, sans-serif; font-weight: 600; color: var(--logo-grey); letter-spacing: 8px; text-transform: uppercase; text-align: center; line-height: 1.15; }

  .claim { position: absolute; font-weight: 700; font-size: 15px; white-space: nowrap; }
  .claim-protein { color: var(--accent-red); }
  .claim-flavour { color: var(--text-white); }
  .net-weight { position: absolute; font-weight: 700; font-size: 17px; white-space: nowrap; }

  .ingredients { position: absolute; left: 80px; top: 76px; width: 520px; font-size: 6.5px; line-height: 10px; }
  .ingredients b { font-weight: 700; }

  .nutrition { position: absolute; left: 95px; top: 455px; width: 200px; height: 74px; background: #fff; color: #000; padding: 4px 5px; display: flex; gap: 6px; font-size: 5px; line-height: 7px; }
  .nutrition h3 { font-size: 8px; line-height: 8px; font-weight: 800; }
  .nutrition table { border-collapse: collapse; width: 104px; }
  .nutrition td, .nutrition th { border-bottom: .5px solid #000; padding: 1px 1px; text-align: left; font-weight: 400; }
  .nutrition th { font-weight: 700; }

  .maker { position: absolute; left: 315px; top: 459px; width: 200px; text-align: center; font-size: 6.5px; line-height: 9px; }
  .proudly { position: absolute; left: 330px; top: 492px; font-size: 9px; font-weight: 700; display: flex; align-items: center; gap: 5px; }
  .social { position: absolute; left: 325px; top: 508px; display: flex; align-items: center; gap: 3px; }
  .social .dot { width: 13px; height: 13px; border-radius: 50%; background: var(--accent-red); }
  .social .site { margin-left: 5px; font-size: 16px; font-weight: 700; color: var(--accent-red); }
</style>
</head>
<body>

<section class="wrapper-front" aria-label="Wrapper front">
  <svg width="1000" height="520" viewBox="0 0 1000 520">
    <defs>
      <linearGradient id="sheen" x1="0" y1="0" x2="0" y2="1">
        <stop offset="0" stop-color="#2a2a2a"/>
        <stop offset=".12" stop-color="#0b0b0b"/>
        <stop offset=".85" stop-color="#0b0b0b"/>
        <stop offset=".95" stop-color="#3a3a3a"/>
        <stop offset="1" stop-color="#141414"/>
      </linearGradient>
      <radialGradient id="ember" cx="690" cy="400" r="120" gradientUnits="userSpaceOnUse" gradientTransform="translate(0 260) scale(1 .35)">
        <stop offset="0" stop-color="#ffd27a"/>
        <stop offset=".35" stop-color="#ff7a1a"/>
        <stop offset="1" stop-color="#7a1e08" stop-opacity="0"/>
      </radialGradient>
      <radialGradient id="forgeGlow" cx="680" cy="320" r="200" gradientUnits="userSpaceOnUse">
        <stop offset="0" stop-color="#5a2a16" stop-opacity=".7"/>
        <stop offset="1" stop-color="#0b0b0b" stop-opacity="0"/>
      </radialGradient>
      <pattern id="teeth" width="8" height="10" patternUnits="userSpaceOnUse">
        <polygon points="0,0 8,5 0,10" fill="#ffffff"/>
      </pattern>
      <pattern id="teethRight" width="8" height="10" patternUnits="userSpaceOnUse">
        <polygon points="8,0 0,5 8,10" fill="#ffffff"/>
      </pattern>
    </defs>
    <path class="wrapper-body" d="M108,162 Q500,218 893,162 L893,486 Q500,432 108,486 Z" fill="url(#sheen)"/>
    <rect x="108" y="160" width="45" height="330" fill="#161616" opacity=".6"/>
    <rect x="848" y="160" width="45" height="330" fill="#161616" opacity=".6"/>
    <rect x="104" y="158" width="8" height="332" fill="url(#teeth)"/>
    <rect x="889" y="158" width="8" height="332" fill="url(#teethRight)"/>
    <g role="img" aria-label="Photo of a blacksmith hammer striking glowing hot metal on an anvil">
      <rect x="530" y="205" width="310" height="245" fill="url(#forgeGlow)"/>
      <ellipse cx="690" cy="400" rx="120" ry="42" fill="url(#ember)"/>
    </g>
  </svg>

  <div class="brand-frame" style="left:190px; top:253px; width:346px; height:120px;">
    <span class="brand-name" style="font-size:38px;">Tallow<br><span style="font-size:22px;">Bar</span></span>
  </div>
  <span class="net-weight" style="left:574px; top:308px;">50g bar / barre</span>
  <span class="claim claim-protein" style="left:190px; top:393px;">Hydrolyzed Whey Protein</span>
  <span class="claim claim-flavour" style="left:400px; top:393px;">Maple Oat Crunch</span>
</section>

<section class="flat-label" aria-label="Wrapper flat label">
  <span class="seam" style="top:46px;"></span>
  <span class="seam" style="top:442px;"></span>
  <span class="seam-side" style="left:48px;"></span>
  <span class="seam-side" style="right:48px;"></span>

  <div class="forge-scene label-scene" role="img" aria-label="Photo of a blacksmith hammer striking glowing hot metal on an anvil"></div>

  <p class="ingredients"><b>Ingredients:</b> Peas are growing in popularity as a sustainable protein source for the global food industry.<br>
  Our pea protein isolate is currently sourced overseas. We are working on finding a suitable supplier on the Canadian Prairies!<br>
  <b>Contains:</b> Milk, Peanuts</p>

  <div class="brand-frame" style="left:87px; top:220px; width:338px; height:125px;">
    <span class="brand-name" style="font-size:38px;">Tallow<br><span style="font-size:22px;">Bar</span></span>
  </div>
  <span class="net-weight" style="left:459px; top:272px;">50g bar / barre</span>
  <span class="claim claim-protein" style="left:90px; top:354px;">Hydrolyzed Whey Protein</span>
  <span class="claim claim-flavour" style="left:293px; top:354px;">Maple Oat Crunch</span>

  <div class="nutrition">
    <div>
      <h3>Nutrition<br>Facts</h3>
      <p>Serving Size 1 Pouch (110g)<br>Serving Per Container 1</p>
      <p style="margin-top:2px;"><b>Calories</b> 80<br>&nbsp;&nbsp;&nbsp;&nbsp;Calories from Fat 5</p>
    </div>
    <table>
      <tr><th>Amount/Serving</th><th>%Daily Value</th></tr>
      <tr><th>Total Fat &nbsp;0g</th><td>0%</td></tr>
      <tr><td>&nbsp;&nbsp;Sat Fat 0g</td><td>0%</td></tr>
      <tr><td>&nbsp;&nbsp;Trans Fat 0g</td><td>0%</td></tr>
      <tr><th>Total Carb &nbsp;18g</th><td>6%</td></tr>
      <tr><th>Protein &nbsp;25g</th><td>0%</td></tr>
    </table>
  </div>

  <p class="maker">Prairie Foundry Foods Inc.<br>18 Anvil Lane<br>Regina, SK S4P 1A1, Canada</p>

  <div class="proudly">Proudly Canadian
    <svg width="20" height="11" viewBox="0 0 20 11" aria-label="Canadian flag">
      <rect width="20" height="11" fill="#fff"/>
      <rect width="5" height="11" fill="#e0262a"/>
      <rect x="15" width="5" height="11" fill="#e0262a"/>
      <polygon points="10,2.2 11.4,5 13,4.6 12,7.4 10.4,7.2 10.4,9 9.6,9 9.6,7.2 8,7.4 7,4.6 8.6,5" fill="#e0262a"/>
    </svg>
  </div>

  <div class="social">
    <span class="dot"></span><span class="dot"></span><span class="dot"></span>
    <span class="site">tallowbarco.ca</span>
  </div>
</section>

</body>
</html>
```